HVL Regal Business Card Design 2020

Harbor Vale Living is looking for a business card that is clean and straight to the point but still looks high-end and attractive. We are a team comprised of management and field professionals focused on the high-end residential marketplace. We serve homeowners and trade professionals directly based out of the Metrowest/Boston area. We provide client services as well as construction/renovation services.
We are aiming for a black and white feel (white background and black text) and a matte finish with rounded edges.

We want to emphasis our vision of "Properties - Projects - Partners".
Dana Pritchell is the president of HVL

Please include the following areas we service: Boston/Cape/Newport
Please make sure to include Dana's mobile (617) 555 0143 & office number (617) 555 0187, email dana@harborvaleliving.example and website www.harborvaleliving.example

Colors

Designer to choose only greyscale colors for use in the design.

Requirements
Must have
• Include "Properties - Projects - Partners" in design

Include "After Hours Emergency Support # 1800 555 0199" with icon

```html
<!DOCTYPE html>
<html lang="en">
<head>
<meta charset="utf-8">
<title>Harbor Vale Living – Business Card</title>
<link href="https://fonts.googleapis.com/css2?family=Source+Sans+3:wght@400;600;700&family=Open+Sans:wght@400&display=swap" rel="stylesheet">
<style>
  :root {
    --backdrop-center: #f1f1f1;
    --backdrop-edge: #d9d9d9;
    --card: #f5f5f5;
    --ink: #231f20;
    --ink-soft: #2b2b2b;
    --shadow: rgba(0, 0, 0, 0.35);
  }
  * { margin: 0; padding: 0; box-sizing: border-box; }
  html, body { width: 1200px; height: 960px; overflow: hidden; }
  body {
    position: relative;
    background: radial-gradient(ellipse at 50% 50%, var(--backdrop-center) 0%, var(--backdrop-edge) 75%);
    font-family: "Source Sans 3", "Myriad Pro", Arial, sans-serif;
    color: var(--ink);
  }
  .card {
    position: absolute;
    left: 310px;
    width: 581px;
    height: 333px;
    background: var(--card);
    box-shadow: 2px 3px 5px var(--shadow);
  }
  .card--front { top: 127px; }
  .card--back { top: 511px; height: 332px; }

  .wordmark {
    position: absolute;
    font-family: "Source Sans 3", Arial, sans-serif;
    font-weight: 700;
    color: var(--ink);
    line-height: 1;
    white-space: nowrap;
  }
  .card--front .wordmark {
    left: 0; right: 0; top: 88px;
    text-align: center;
    font-size: 172px;
    letter-spacing: -3px;
  }
  .tagline {
    position: absolute;
    left: 0; right: 0; top: 287px;
    text-align: center;
    font-family: "Open Sans", Arial, sans-serif;
    font-size: 14px;
    letter-spacing: 1.5px;
    color: var(--ink-soft);
  }

  .brand-block {
    position: absolute;
    left: 40px; top: 104px;
    width: 220px;
    text-align: center;
  }
  .card--back .wordmark {
    position: static;
    display: block;
    font-size: 104px;
    letter-spacing: -1px;
  }
  .brand-name {
    display: block;
    margin-top: 0;
    font-weight: 700;
    font-size: 13.5px;
    letter-spacing: 2.6px;
    text-transform: uppercase;
  }
  .divider {
    position: absolute;
    left: 289px; top: 96px;
    width: 2px; height: 138px;
    background: var(--ink);
  }
  .contact {
    position: absolute;
    left: 322px; top: 96px;
  }
  .contact__name {
    font-weight: 700;
    font-size: 19px;
    line-height: 24px;
  }
  .contact__role {
    font-size: 14px;
    line-height: 17px;
    margin-bottom: 17px;
  }
  .contact__list { list-style: none; }
  .contact__item {
    display: flex;
    align-items: center;
    gap: 4px;
    font-size: 15px;
    line-height: 19.5px;
  }
  .contact__icon { width: 13px; height: 13px; flex: none; }
  .emergency {
    position: absolute;
    left: 0; right: 0; top: 256px;
    display: flex;
    justify-content: center;
    align-items: center;
    gap: 5px;
    font-size: 13px;
    line-height: 16px;
  }
  .service-areas {
    position: absolute;
    left: 0; right: 0; top: 286px;
    text-align: center;
    font-size: 16px;
  }
</style>
</head>
<body>
  <section class="card card--front">
    <span class="wordmark">HVL</span>
    <p class="tagline">PROPERTIES - PROJECTS - PARTNERS</p>
  </section>

  <section class="card card--back">
    <div class="brand-block">
      <span class="wordmark">HVL</span>
      <span class="brand-name">Harbor Vale Living</span>
    </div>
    <div class="divider"></div>
    <div class="contact">
      <p class="contact__name">Dana Pritchell</p>
      <p class="contact__role">President</p>
      <ul class="contact__list">
        <li class="contact__item">
          <svg class="contact__icon" viewBox="0 0 13 13" aria-hidden="true"><rect x="3" y="0.8" width="7" height="11.4" rx="1.2" fill="none" stroke="#231f20" stroke-width="1.3"/><rect x="5.5" y="10" width="2" height="1" fill="#231f20"/></svg>
          (617) 555 0143
        </li>
        <li class="contact__item">
          <svg class="contact__icon" viewBox="0 0 13 13" aria-hidden="true"><path d="M2.6 0.8 L4.8 0.6 L5.6 3.6 L4.2 4.8 C5 6.6 6.4 8 8.2 8.8 L9.4 7.4 L12.4 8.2 L12.2 10.4 C11.8 11.8 10.6 12.4 9.2 12 C5.2 10.8 2.2 7.8 1 3.8 C0.6 2.4 1.2 1.2 2.6 0.8 Z" fill="#231f20"/></svg>
          (617) 555 0187
        </li>
        <li class="contact__item">
          <svg class="contact__icon" viewBox="0 0 13 13" aria-hidden="true"><rect x="0.7" y="2.5" width="11.6" height="8" fill="none" stroke="#231f20" stroke-width="1.3"/><path d="M0.7 2.5 L6.5 7.2 L12.3 2.5" fill="none" stroke="#231f20" stroke-width="1.3"/></svg>
          dana@harborvaleliving.example
        </li>
        <li class="contact__item">
          <svg class="contact__icon" viewBox="0 0 13 13" aria-hidden="true"><circle cx="6.5" cy="6.5" r="5.7" fill="none" stroke="#231f20" stroke-width="1.2"/><ellipse cx="6.5" cy="6.5" rx="2.5" ry="5.7" fill="none" stroke="#231f20" stroke-width="1"/><path d="M0.8 6.5 H12.2 M1.8 3.6 H11.2 M1.8 9.4 H11.2" stroke="#231f20" stroke-width="1"/></svg>
          www.harborvaleliving.example
        </li>
      </ul>
    </div>
    <p class="emergency">
      <svg class="contact__icon" viewBox="0 0 13 13" aria-hidden="true"><circle cx="6.5" cy="6.5" r="5.8" fill="#231f20"/><rect x="5.8" y="2.8" width="1.4" height="4.8" fill="#f5f5f5"/><rect x="5.8" y="8.8" width="1.4" height="1.4" fill="#f5f5f5"/></svg>
      After Hours Emergency Support # 1800 555 0199
    </p>
    <p class="service-areas">Boston | Metrowest | South Shore | Cape | Newport</p>
  </section>
</body>
</html>
```